Business card design needed

I need a business card for a new company based in Perth, Western Australia, called KT Power Pty Ltd.

I'm the sole proprietor, and have 25 years' experience in directorship, senior commercial/business development/strategy roles in the oil & gas industry with both supermajors and junior listed companies. I also have interests in renewable energy (and am co-founder and director of a separate renewable energy start-up company). KT Power will be the vehicle for me to contract my services, principally in the oil & gas industry (although this will include directorship services to the renewable energy company). These services will include general consultancy in my areas of expertise, and contracting to provide senior management/director services to start-up or junior oil and gas companies.

I'm looking for a design that communicates professionalism, dynamism, experience, strategic skills and growth.

My Proflinker profile may also be useful context;

"I have a real passion for discovering new investment opportunities and turning them from talk into reality. Right now my focus is on oil, gas and energy ventures. I’m always on the look out for compelling new investment opportunities where I can bring my leadership and strategic insight to bear to make a real difference by delivering transformational results.

I spent 24 years with NX where I built up extensive international experience in oil, gas and energy and was a member of the company’s “fast track” development programme. As an entrepreneurial senior commercial leader, strategic thinker and tactical dealmaker I was responsible for numerous deals such as divestments, farm-ins, asset swaps, new acreage bids, unitizations, gas and LNG sales, creating billions of dollars of value for NX. These deals frequently broke new ground and/or required an innovative approach that delivered results in excess of what the business thought achievable. I have held senior executive and director roles covering Exploration & Production, Mergers & Acquisitions, Business Development, LNG Marketing, Joint Venture Management, Gas & Power and Corporate head office. International assignments included UK, Australia, Indonesia, Norway & Belgium.

I’m a member of the Guild of Global Fuel Brokers (GGFB) and the National Council of Board Officers (NCBO).

Board experience comprises four directorships and two alternate directorships of Australian companies, and directorship of a Not for Profit organisation.

Specialties
Strategy, Business Development, Mergers & Acquisitions, Joint Venture Management, Negotiation, Gas & LNG Marketing."

Target Market(s)

Oil and gas or energy companies of all sizes from large listed companies to start-ups - also service providers to the industry.

Industry/Entity Type

Oil And Gas

Contact Information for Business Card

KT Power Pty Ltd
Martin Dacombe
27C Ferncliff Road,
Holloway Vale,
WA 6999

Tel +61 400 555 817
email dacombemj@quenvol.example.au

```html
<!DOCTYPE html>
<html lang="en">
<head>
<meta charset="utf-8">
<title>KT Power Pty Ltd — Business Card</title>
<link rel="stylesheet" href="https://fonts.googleapis.com/css2?family=Fira+Sans:wght@300;400;500&display=swap">
<style>
  :root {
    --backdrop: #d6d6d6;
    --card: #3b3b3b;
    --ink: #e8e8e8;
    --ink-soft: #bdbdbd;
    --rule: #cfcfcf;
  }
  * { box-sizing: border-box; margin: 0; padding: 0; }
  html, body {
    width: 1200px;
    height: 747px;
    overflow: hidden;
    background: var(--backdrop);
    font-family: "Fira Sans", sans-serif;
    color: var(--ink);
  }
  .sheet {
    width: 1200px;
    height: 747px;
    display: flex;
    justify-content: center;
    align-items: center;
    gap: 70px;
  }
  .card {
    width: 350px;
    height: 610px;
    background: var(--card);
    display: flex;
    flex-direction: column;
    align-items: center;
    text-align: center;
    padding: 62px 30px 50px;
  }
  .holder-name {
    font-size: 23px;
    font-weight: 500;
    letter-spacing: 0.2px;
  }
  .divider {
    display: block;
    width: 230px;
    height: 10px;
  }
  .divider--top { margin-top: 70px; }
  .divider--bottom { margin-top: 26px; }
  .contact {
    margin-top: 20px;
    font-size: 19px;
    font-weight: 300;
    line-height: 1.3;
  }
  .contact .label { font-weight: 500; }
  .address {
    margin-top: 22px;
    font-size: 19px;
    font-weight: 300;
    line-height: 1.25;
  }
  .address .company { font-weight: 500; }
  .membership-note {
    margin-top: 38px;
    font-size: 15px;
    font-weight: 300;
    color: var(--ink-soft);
  }
  .council-name {
    margin-top: 30px;
    font-size: 19px;
    font-weight: 400;
    text-transform: uppercase;
    letter-spacing: 1.2px;
    line-height: 1.05;
  }
  .guild-mark {
    margin-top: 28px;
    display: flex;
    align-items: center;
    gap: 10px;
    font-size: 24px;
    font-weight: 500;
    letter-spacing: 1px;
  }
  .guild-mark .dot {
    width: 40px;
    height: 40px;
    border: 1.5px solid var(--ink);
    border-radius: 50%;
  }
  .brand-mark {
    margin-top: 70px;
    display: flex;
    align-items: center;
    gap: 10px;
    font-size: 22px;
    font-weight: 400;
    letter-spacing: 0.5px;
  }
  .brand-mark .dot {
    width: 12px;
    height: 12px;
    background: var(--ink);
    border-radius: 50%;
  }
  .specialties {
    margin-top: auto;
    margin-bottom: 34px;
    list-style: none;
    font-size: 21px;
    font-weight: 400;
    line-height: 1.55;
  }
  .specialties li::before { content: "• "; color: var(--ink-soft); }
  .specialties li::after { content: " •"; color: var(--ink-soft); }
</style>
</head>
<body>
  <main class="sheet">
    <section class="card card--front">
      <h1 class="holder-name">Martin Dacombe</h1>

      <svg class="divider divider--top" viewBox="0 0 230 10" aria-hidden="true">
        <line x1="0" y1="5" x2="230" y2="5" stroke="#cfcfcf" stroke-width="1.2"/>
        <circle cx="115" cy="5" r="3.5" fill="#cfcfcf"/>
      </svg>

      <p class="contact">
        <span class="label">t:</span> +61 400 555 817<br>
        <span class="label">e:</span> dacombemj@quenvol.example.au
      </p>

      <p class="address">
        <span class="company">KT Power Pty Ltd</span><br>
        27C Ferncliff Road<br>
        Holloway Vale, WA 6999
      </p>

      <svg class="divider divider--bottom" viewBox="0 0 230 10" aria-hidden="true">
        <line x1="0" y1="5" x2="230" y2="5" stroke="#cfcfcf" stroke-width="1.2"/>
        <circle cx="115" cy="5" r="3.5" fill="#cfcfcf"/>
      </svg>

      <p class="membership-note">memeber of</p>

      <p class="council-name">National Council<br>of Board Officers</p>

      <p class="guild-mark"><span class="dot" aria-hidden="true"></span>GGFB</p>
    </section>

    <section class="card card--back">
      <p class="brand-mark"><span class="dot" aria-hidden="true"></span>KT Power</p>

      <ul class="specialties">
        <li>Strategy</li>
        <li>Business Development</li>
        <li>Mergers &amp; Acquisitions</li>
        <li>Joint Venture Management</li>
        <li>Negotiation</li>
        <li>Gas &amp; LNG Marketing</li>
      </ul>
    </section>
  </main>
</body>
</html>
```